Web Design Project for velbrook

We are looking for a sleek and sophisticated website design for our already developed web-based gallery management software application. Here is a link to our web-app: http://www.vel-brook.co

You will login on the main page and then we would like to include all of the information on the PDF that I am providing below (it outlines what?, where?, why? who? and how much?). Basically, we need a home page, about page, and a pricing page, as well as a sign up page that should be navigable from the upper right hand corner of the site where the sign in/sign up would be located. Also, our 3 tenets are that the software program is "attractive, accessible, and affordable", which might need to be somehow incorporated. There are a few websites that we would like for you to take inspiration from listed below:

https://tidemoxen.com (for homepage)
https://plumwovenly.com (for homepage/pricing page/etc)
https://tidemoxen.com/tour (for a tour of how the product works)

We are currently having a logo designed and will share that as soon as it is available! Also, let us know if you need photos/screen shots, as we can provide them.

Thanks!

Reason: Extending deadline as we are just now getting designs we would like to see fully developed.

Target Market(s)

art galleries, artists, art collectors, art consultants, museums

Industry/Entity Type

Software

Requirements
Must have
• Home page
About page (or tour through the app)
Pricing page
Sign up page (the more click-throughs to signing up the better)

```html
<!DOCTYPE html>
<html lang="en">
<head>
<meta charset="utf-8">
<title>velbrook – Gallery Management in the Cloud</title>
<link rel="stylesheet" href="https://fonts.googleapis.com/css2?family=Quicksand:wght@400;500;600&family=Arimo:wght@400;700&display=swap">
<style>
  :root {
    --brand-blue: #3bb7e6;
    --ink: #1a1a1a;
    --body-ink: #222222;
    --paper: #f7f7f7;
    --band: #e9e9e9;
    --orange: #f07c14;
    --dark: #2c2c2c;
    --footer: #262626;
    --white: #ffffff;
    --link: #2a8fd6;
  }
  * { box-sizing: border-box; margin: 0; padding: 0; }
  html, body { width: 1200px; height: 3175px; overflow: hidden; }
  body {
    position: relative;
    background: var(--paper);
    font-family: "Arimo", Arial, sans-serif;
    color: var(--body-ink);
  }
  .site-header {
    position: absolute; left: 0; top: 0; width: 1200px; height: 90px;
    background: var(--white);
    display: flex; align-items: center; justify-content: space-between;
    padding: 0 25px 0 20px;
  }
  .brand { display: flex; align-items: center; gap: 10px;
    font-family: "Quicksand", sans-serif; font-weight: 500; font-size: 44px; color: var(--brand-blue); }
  .brand-dot { width: 30px; height: 30px; border-radius: 50%; background: var(--brand-blue); }
  .main-nav { display: flex; align-items: center; gap: 34px;
    font-family: "Quicksand", sans-serif; font-weight: 600; font-size: 31px; color: var(--ink); }
  .main-nav .nav-signup { background: var(--brand-blue); color: var(--white); padding: 4px 12px; border-radius: 4px; }

  .hero {
    position: absolute; left: 0; top: 90px; width: 1200px; height: 655px;
    background: linear-gradient(100deg, #3a3a38 0%, #8d8a84 30%, #c9c6c0 55%, #6d6a64 80%, #2f2f2d 100%);
  }
  .hero-title {
    position: absolute; left: 25px; top: 178px; width: 860px;
    font-family: "Quicksand", sans-serif; font-weight: 500; font-size: 58px; line-height: 70px;
    color: var(--white);
  }

  .about-tab {
    position: absolute; left: 248px; top: 715px; width: 704px; height: 115px;
    background: var(--dark); border-radius: 10px;
    display: flex; align-items: center; justify-content: center;
    font-family: "Quicksand", sans-serif; font-size: 56px; color: var(--white);
  }

  .info-band { position: absolute; left: 0; top: 1490px; width: 1200px; height: 545px; background: var(--band); }

  .info { position: absolute; left: 25px; width: 1160px; }
  .info h2 { font-family: "Arimo", Arial, sans-serif; font-weight: 400; font-size: 38px; line-height: 44px; color: var(--ink); }
  .info p { font-size: 26px; line-height: 36px; }
  .info p + p { margin-top: 36px; }
  .info a { color: var(--link); text-decoration: none; }

  .signup-small { position: absolute; left: 497px; width: 200px; text-align: center; }
  .signup-small .btn {
    display: block; height: 54px; background: var(--orange); color: var(--white);
    font-family: "Quicksand", sans-serif; font-weight: 600; font-size: 40px; line-height: 54px;
  }
  .signup-small .note { display: block; font-size: 17px; line-height: 22px; color: var(--ink); }

  .cta-large {
    position: absolute; left: 248px; top: 2597px; width: 704px; height: 113px;
    background: var(--orange); border-radius: 10px;
    display: flex; align-items: center; justify-content: center;
    font-family: "Quicksand", sans-serif; font-size: 56px; color: var(--white);
  }

  .site-footer { position: absolute; left: 0; top: 2785px; width: 1200px; height: 390px; background: var(--footer); color: var(--white);
    font-family: "Quicksand", sans-serif; }
  .footer-nav { position: absolute; left: 50px; top: 80px; font-size: 28px; line-height: 41px; list-style: none; }
  .footer-contact { position: absolute; left: 430px; top: 80px; font-size: 28px; line-height: 41px; font-style: normal; }
  .footer-contact .label { margin-bottom: 18px; }
  .footer-contact .gap { margin-top: 12px; }
  .footer-contact .street { margin-top: 12px; line-height: 34px; }
  .social { position: absolute; top: 100px; width: 72px; height: 72px; border-radius: 50%; background: var(--brand-blue); }
  .social.one { left: 868px; }
  .social.two { left: 976px; }
  .footer-legal { position: absolute; left: 50px; top: 355px; font-size: 21px; }
</style>
</head>
<body>
  <header class="site-header">
    <div class="brand"><span class="brand-dot"></span>velbrook</div>
    <nav class="main-nav">
      <span>Home</span><span>About</span><span>Pricing</span><span class="nav-signup">Sign Up</span><span>Log In</span>
    </nav>
  </header>

  <section class="hero" role="img" aria-label="Photo of a white-walled art gallery interior with framed artworks">
    <h1 class="hero-title">velbrook is the easiest way to manage your art data in the cloud.</h1>
  </section>

  <div class="about-tab">About velbrook</div>

  <div class="info-band"></div>

  <section class="info" style="top:865px">
    <h2>What?</h2>
    <p>velbrook is one of the only truly web-based gallery management software systems currently available for galleries, artists, consultants and collectors. On a basic level, it allows you to manage your artists, art inventory, clients, and invoices in one clean interface that is highly integrated. This integration allows for searchability, recordability and exportation of information, all increasing efficiency. Some of the features include pages dedicated to creating art inventory with images, new modules for clients with activity and interest logs, and invoices/approvals with functionality alerting you when payments are due or follow-up contact needs to be made. Also, as a web-based system, velbrook can be viewed on your mobile phone/tablet device. velbrook is the easiest way to manage your art data on the cloud.</p>
  </section>

  <section class="info" style="top:1250px">
    <h2>Where?</h2>
    <p>velbrook is hosted on our state-of-the art secure server that is available from anywhere via our website. To access your account, simply login through our webpage using your customized username and password. You can connect anytime/anywhere from your laptop, desktop, phone or tablet device with a simple internet connection.</p>
  </section>

  <div class="signup-small" style="top:1436px"><span class="btn">Sign Up</span><span class="note">60 Days FREE</span></div>

  <section class="info" style="top:1535px">
    <h2>Why?</h2>
    <p>velbrook is attractive, accessible, and affordable. we have developed a system with a clean design that is easy to use, can be accessed from anywhere in the world anytime day or night, and is less expensive than any other similar product currently on the market. velbrook's sleek interface will be appreciated by your clients and artists. The simplified and pared down platform will allow you to quickly and efficiently add inventory, look up clients' past purchases, and export reports for sales. And the attractive price point is just an added bonus.</p>
    <p>velbrook comes with free support, free upgrades, and an innovative virtual sales manager that will help to grow your business, all for a fixed monthly fee. Click here for pricing. (we don't know where you will want to put pricing—on the sign-up page or on the about page—so we may need to click through here)</p>
  </section>

  <div class="signup-small" style="top:2054px"><span class="btn">Sign Up</span><span class="note">60 Days FREE</span></div>

  <section class="info" style="top:2127px">
    <h2>How much?</h2>
    <p>velbrook is one of the most affordable gallery database options on the marketplace with an initial activation fee of $500 and a modest monthly maintenance fee of $99. That's it, and with that is included system set-up if using our import template, support, hosting, back-up and any upgrades to improve the system. Click here to sign-up.</p>
  </section>

  <section class="info" style="top:2390px">
    <h2>Want to Sign Up?</h2>
    <p>Need help getting started? Want assistance uploading your client list, art inventory, or past sales? <a href="#">Email us here.</a></p>
  </section>

  <div class="cta-large">Click Here to Get Started</div>

  <footer class="site-footer">
    <ul class="footer-nav">
      <li>Home</li><li>About</li><li>Pricing</li><li>Sign Up</li><li>Log In</li>
    </ul>
    <address class="footer-contact">
      <div class="label">Contact Us</div>
      <div>help@velbrook.co</div>
      <div class="gap">(555) 410-2276</div>
      <div class="street">88 Linden Row<br>Marlow Bay, OR<br>97031</div>
    </address>
    <span class="social one" aria-label="Social profile"></span>
    <span class="social two" aria-label="Social profile"></span>
    <div class="footer-legal">velbrook 2013 – Sitemap</div>
  </footer>
</body>
</html>
```